SHG business cards

design a business card

(Generators . Lighting Towers . De-watering Pumps . Compressors) put under the logo please. my details are Marek Oyelaran (Director) 0461527308 silverpinehaulgroup@postvane.com

```html
<!DOCTYPE html>
<html lang="en">
<head>
<meta charset="utf-8">
<title>SHG Business Cards</title>
<link href="https://fonts.googleapis.com/css2?family=Montserrat:wght@500;700&family=Arimo:wght@400&display=swap" rel="stylesheet">
<style>
  :root {
    --backdrop: #c9c9c9;
    --card: #1b1b1c;
    --card-edge: #111112;
    --gold: #e3a02a;
    --gold-deep: #b97a14;
    --silver: #cfd0d2;
    --silver-deep: #8d8e91;
    --text-light: #e9e9ea;
    --rule: #6b6b6d;
    --pattern-a: #2a2a2c;
    --pattern-b: #121213;
  }
  * { box-sizing: border-box; margin: 0; padding: 0; }
  html, body { width: 1200px; height: 788px; overflow: hidden; }
  body {
    background: var(--backdrop);
    font-family: "Arimo", Arial, sans-serif;
    display: flex;
    align-items: center;
    justify-content: center;
    gap: 40px;
  }
  .card {
    position: relative;
    width: 540px;
    height: 310px;
    border-radius: 18px;
    background: var(--card);
    overflow: hidden;
    box-shadow: 0 10px 26px rgba(0,0,0,.28);
  }
  .card-band {
    position: absolute;
    left: 0; right: 0; bottom: 0;
    height: 34px;
  }
  .card-band svg { display: block; width: 100%; height: 100%; }

  /* front */
  .brand {
    position: absolute;
    top: 46px; left: 0; right: 0;
    text-align: center;
  }
  .brand-mark {
    display: inline-flex;
    align-items: center;
    gap: 10px;
    font-family: "Montserrat", sans-serif;
    font-weight: 700;
    color: var(--gold);
    letter-spacing: 2px;
  }
  .brand-square {
    width: 22px; height: 22px;
    background: var(--gold);
  }
  .brand-initials { font-size: 30px; }
  .brand-name {
    margin-top: 8px;
    font-family: "Montserrat", sans-serif;
    font-weight: 700;
    font-size: 22px;
    color: var(--gold);
    letter-spacing: 1.5px;
    text-transform: uppercase;
  }
  .details {
    position: absolute;
    top: 156px; left: 0; right: 0;
    display: flex;
    justify-content: center;
    align-items: center;
    gap: 22px;
  }
  .person { text-align: right; }
  .person-name {
    font-family: "Montserrat", sans-serif;
    font-weight: 700;
    font-size: 19px;
    color: var(--gold);
    text-transform: uppercase;
    letter-spacing: .5px;
  }
  .person-role {
    font-size: 13px;
    color: var(--text-light);
    margin-top: 4px;
  }
  .divider {
    width: 1px; height: 46px;
    background: var(--rule);
  }
  .contact { list-style: none; }
  .contact li {
    display: flex;
    align-items: center;
    gap: 7px;
    font-size: 12.5px;
    color: var(--text-light);
    line-height: 1.8;
  }
  .contact svg { width: 11px; height: 11px; fill: var(--gold); flex: none; }
  .services {
    position: absolute;
    left: 0; right: 0; bottom: 52px;
    text-align: center;
    font-family: "Montserrat", sans-serif;
    font-weight: 500;
    font-size: 10.5px;
    letter-spacing: .6px;
    color: var(--text-light);
    text-transform: uppercase;
  }

  /* back */
  .pattern {
    position: absolute;
    inset: 0;
    background: linear-gradient(115deg, var(--pattern-a) 0%, var(--pattern-b) 55%, var(--pattern-b) 100%);
  }
  .back .brand { top: 104px; }
</style>
</head>
<body>

  <section class="card front" aria-label="Business card front">
    <div class="brand">
      <div class="brand-mark"><span class="brand-square"></span><span class="brand-initials">SHG</span></div>
      <div class="brand-name">Silver Pine Haul Group</div>
    </div>

    <div class="details">
      <div class="person">
        <p class="person-name">Marek Oyelaran</p>
        <p class="person-role">Director</p>
      </div>
      <span class="divider"></span>
      <ul class="contact">
        <li>
          <svg viewBox="0 0 24 24" aria-hidden="true"><path d="M6.6 10.8a15.1 15.1 0 0 0 6.6 6.6l2.2-2.2a1 1 0 0 1 1-.25 11.4 11.4 0 0 0 3.6.57 1 1 0 0 1 1 1V20a1 1 0 0 1-1 1A17 17 0 0 1 3 4a1 1 0 0 1 1-1h3.5a1 1 0 0 1 1 1c0 1.25.2 2.45.57 3.57a1 1 0 0 1-.25 1z"/></svg>
          0461527308
        </li>
        <li>
          <svg viewBox="0 0 24 24" aria-hidden="true"><path d="M2 9l10-6 10 6v11a1 1 0 0 1-1 1H3a1 1 0 0 1-1-1zm3 1.2l7 4.3 7-4.3L12 6z"/></svg>
          silverpinehaulgroup@postvane.com
        </li>
      </ul>
    </div>

    <p class="services">Generators · Lighting Towers · De-watering Pumps · Compressors</p>

    <div class="card-band">
      <svg viewBox="0 0 540 34" preserveAspectRatio="none" aria-hidden="true">
        <polygon points="0,22 380,22 392,10 540,10 540,34 0,34" fill="var(--silver-deep)"/>
        <polygon points="0,24 540,24 540,34 0,34" fill="var(--gold)"/>
        <polygon points="392,10 540,10 540,24 378,24" fill="var(--silver)"/>
        <g stroke="var(--silver)" stroke-width="2">
          <line x1="360" y1="22" x2="368" y2="12"/>
          <line x1="366" y1="22" x2="374" y2="12"/>
          <line x1="372" y1="22" x2="380" y2="12"/>
        </g>
      </svg>
    </div>
  </section>

  <section class="card back" aria-label="Business card back">
    <div class="pattern" role="img" aria-label="Repeating tone-on-tone company monogram pattern"></div>
    <div class="brand">
      <div class="brand-mark"><span class="brand-square"></span><span class="brand-initials">SHG</span></div>
      <div class="brand-name">Silver Pine Haul Group</div>
    </div>
    <div class="card-band">
      <svg viewBox="0 0 540 34" preserveAspectRatio="none" aria-hidden="true">
        <polygon points="0,24 540,24 540,34 0,34" fill="var(--gold)"/>
        <polygon points="392,10 540,10 540,24 378,24" fill="var(--silver)"/>
        <g stroke="var(--silver)" stroke-width="2">
          <line x1="360" y1="22" x2="368" y2="12"/>
          <line x1="366" y1="22" x2="374" y2="12"/>
          <line x1="372" y1="22" x2="380" y2="12"/>
        </g>
      </svg>
    </div>
  </section>

</body>
</html>
```